Flyer für Flugunternehmen
Zielgruppe
Wir sind ein Flugunternehmen, das Rundflüge ab Lübeck anbietet und dabei auf verschiedenen Routen beispielsweise die Lübecker Bucht, Hamburg oder auch Fehmarn ansteuert. Die Zielgruppe ist recht umfangreich und reicht von Urlaubsgästen jeden Alters bis zu Einwohnern, die Ihre Gegend von oben sehen wollen.
Aufgabenstellung
Die Flyer sollen am besten zwei bis drei Routen abbilden und das einzigartige Erlebnis eines Rundfluges verdeutlichen. Preise sollen auf den Flyern noch nicht stehen. Hier ist die 'Weiterleitung' auf unsere Webseite denkbar. Die Firmierung soll lediglich Möwenkamp-Luftreisen lauten und im Kleingedruckten der tatsächliche Name wie im Impressum angegeben.
Der neue Flyer soll den alten Trifold-Flyer im A4 Format ablösen mit einem neuen und modernen Design. Der alte Flyer wird als Anhang beigefügt.
- Auflistung der Highlights: Lübeck, Lübecker Bucht, Hamburg oder Fehmarn
- Maximale Passagierzahl: 3
- Dauer: 30 bis 90 Minuten
- Ggf. Kundenbewertung von Zentavo ohne Namen
- Besondere Erlebnisse möglich, die individuell geplant werden können (z.B. Verlobung, Geburtstage)
- Call-to-Action (Bezug auf unsere Webseite)

```html
<!DOCTYPE html>
<html lang="de">
<head>
<meta charset="utf-8">
<title>Möwenkamp-Luftreisen – Rundflüge ab Lübeck</title>
<link href="https://fonts.googleapis.com/css2?family=Montserrat:wght@300;400;600;700;800;900&display=swap" rel="stylesheet">
<style>
  :root{
    --navy:#0d3f73;
    --route:#123f6e;
    --sky-top:#3f66ad;
    --sky-mid:#5a9bd6;
    --sky-low:#7cc3ea;
    --band:#4aaee2;
    --band-deep:#2f86cc;
    --sea-deep:#3a5fa8;
    --white:#ffffff;
    --logo-blue:#1e8fd6;
  }
  *{margin:0;padding:0;box-sizing:border-box}
  html,body{width:1200px;height:848px;overflow:hidden;background:#fff}
  .flyer{
    position:relative;width:1200px;height:848px;overflow:hidden;
    font-family:"Montserrat",Arial,sans-serif;color:var(--white);
    background:linear-gradient(180deg,var(--sky-top) 0%,var(--sky-mid) 35%,var(--sky-low) 58%,var(--sky-low) 60%);
  }
  .info-band{
    position:absolute;left:0;top:507px;width:1200px;height:311px;
    background:linear-gradient(180deg,var(--band) 0%,#58b8e8 40%,var(--band-deep) 100%);
  }
  .foot-band{position:absolute;left:0;top:818px;width:1200px;height:30px;background:var(--sea-deep)}
  .fold{position:absolute;top:0;width:1px;height:848px;background:rgba(255,255,255,.18)}
  .fold--1{left:404px}.fold--2{left:808px}

  .route-map{
    position:absolute;left:40px;top:30px;width:1040px;height:380px;border-radius:20px;
    background:linear-gradient(120deg,rgba(18,63,110,.10) 0%,rgba(18,63,110,.16) 50%,rgba(18,63,110,.08) 100%);
  }

  .brand-disc{
    position:absolute;left:-10px;top:-62px;width:226px;height:226px;border-radius:50%;background:var(--white);
  }
  .brand-name{
    position:absolute;left:10px;top:88px;width:190px;text-align:center;
    font-weight:700;font-size:15px;color:var(--navy);line-height:1.2;
  }
  .brand-dot{position:absolute;left:87px;top:24px;width:34px;height:34px;border-radius:50%;border:4px solid var(--logo-blue)}

  .place{position:absolute;font-weight:900;color:var(--route);white-space:nowrap}
  .place--sylt{left:246px;top:28px;font-size:18px}
  .place--foehr{left:259px;top:76px;font-size:18px}
  .place--ruegen{left:1066px;top:152px;font-size:19px}
  .place--luebeck{left:589px;top:216px;font-size:33px}

  .islands{position:absolute;left:25px;top:200px;color:var(--route)}
  .islands__title{font-weight:900;font-size:21px;margin-bottom:6px}
  .islands__list{list-style:none;display:grid;grid-template-columns:129px auto;row-gap:2px;font-weight:900;font-size:18px}
  .islands__list li::before{content:"• ";}

  .headline{position:absolute;left:431px;top:38px;font-weight:900;font-size:48px;letter-spacing:-.5px;line-height:1}
  .subline{position:absolute;left:431px;top:91px;font-weight:400;font-size:17px}
  .subline strong{font-weight:800}

  .photo{position:absolute;border-radius:50%;border:4px solid var(--white)}
  .photo--city{left:295px;top:196px;width:284px;height:284px;background:radial-gradient(circle at 50% 35%,#c47a5e 0%,#b96a4f 35%,#5d8a55 70%,#3a6a45 100%)}
  .photo--bay{left:581px;top:317px;width:230px;height:230px;background:linear-gradient(160deg,#6b7d5c 0%,#8a8a6a 35%,#d9cdb0 55%,#3d7fb0 70%,#1f4f8f 100%)}
  .photo--harbour{left:829px;top:185px;width:284px;height:284px;background:linear-gradient(180deg,#3d6fbf 0%,#9fc0e0 30%,#8d8a7c 55%,#6b5244 80%,#4a4740 100%)}
  .photo--wing{left:240px;top:677px;width:152px;height:152px;background:linear-gradient(170deg,#6a8fc0 0%,#3b5f8e 40%,#4f5e4a 65%,#d9dee6 100%)}

  .column{position:absolute;top:522px}
  .column--luebeck{left:21px;width:352px}
  .column--bucht{left:431px;width:350px}
  .column--hamburg{left:829px;width:364px}
  .column__title{font-weight:300;font-size:25px;line-height:30px;letter-spacing:.2px}
  .column__title strong{font-weight:900;color:var(--navy)}
  .column__lead{margin-top:9px;font-size:13.4px;line-height:18.4px;font-weight:300}
  .column__lead strong{font-weight:700}
  .highlights{list-style:none;position:absolute;top:168px;left:0;color:var(--navy);font-weight:700;font-size:13.6px;line-height:18.5px;white-space:nowrap}
  .tick{display:inline-block;width:16px;height:13px;vertical-align:-1px;margin-left:2px}

  .badge{position:absolute;width:84px;height:84px;border-radius:50%;background:var(--navy);
    display:flex;flex-direction:column;align-items:center;justify-content:center;text-align:center;
    transform:rotate(-8deg);line-height:1.1}
  .badge__label{font-weight:800;font-size:12px}
  .badge__time{font-weight:800;font-size:12.5px}
  .badge__pax{font-weight:300;font-size:11.5px}
  .badge--30{left:274px;top:494px}
  .badge--45{left:661px;top:701px}
  .badge--60{left:1051px;top:680px}
</style>
</head>
<body>
<div class="flyer">
  <div class="info-band"></div>
  <div class="foot-band"></div>
  <div class="fold fold--1"></div>
  <div class="fold fold--2"></div>

  <div class="route-map" role="img" aria-label="Streckenkarte mit Flugrouten ab Lübeck nach Sylt, Föhr, Rügen und zu den Ostfriesischen Inseln"></div>

  <div class="brand-disc"></div>
  <div class="brand-dot"></div>
  <div class="brand-name">Möwenkamp-Luftreisen</div>

  <div class="place place--sylt">Sylt</div>
  <div class="place place--foehr">Föhr</div>
  <div class="place place--ruegen">Rügen</div>
  <div class="place place--luebeck">Lübeck</div>

  <div class="islands">
    <div class="islands__title">Ostfriesische Inseln</div>
    <ul class="islands__list">
      <li>Borkum</li><li>Baltrum</li>
      <li>Juist</li><li>Langeoog</li>
      <li>Norderney</li><li>Wangerooge</li>
    </ul>
  </div>

  <h1 class="headline">Wir schaffen Erinnerungen.</h1>
  <p class="subline">Weitere Flüge und Infos erhalten Sie unter: <strong>www.moewenkamp-luftreisen.de</strong></p>

  <div class="photo photo--city" role="img" aria-label="Luftbild der Lübecker Altstadtinsel mit roten Dächern und Kirchtürmen"></div>
  <div class="photo photo--harbour" role="img" aria-label="Luftbild des Hamburger Hafens mit Speicherstadt an der Elbe"></div>
  <div class="photo photo--bay" role="img" aria-label="Luftbild der Lübecker Bucht mit Strand, Seebrücke und Ostsee"></div>

  <section class="column column--luebeck">
    <h2 class="column__title">Über den Dächern<br><strong>Lübecks.</strong></h2>
    <p class="column__lead"><strong>Warum Lübeck zum UNESCO-Welterbe zählt? Steigen Sie ein und finden Sie es heraus!</strong> Ihr Rundflug führt Sie über die historisch bedeutende Hansestadt Lübeck mit seiner faszinierenden Stadtinsel.</p>
    <ul class="highlights">
      <li>Altstadt Lübeck <svg class="tick" viewBox="0 0 16 13"><path d="M2 7 L6 11 L14 1" stroke="#0d3f73" stroke-width="3" fill="none"/></svg></li>
      <li>Rathaus <svg class="tick" viewBox="0 0 16 13"><path d="M2 7 L6 11 L14 1" stroke="#0d3f73" stroke-width="3" fill="none"/></svg></li>
      <li>Kirchen auf der Stadtinsel <svg class="tick" viewBox="0 0 16 13"><path d="M2 7 L6 11 L14 1" stroke="#0d3f73" stroke-width="3" fill="none"/></svg></li>
      <li>Salzspeicher an der Trave <svg class="tick" viewBox="0 0 16 13"><path d="M2 7 L6 11 L14 1" stroke="#0d3f73" stroke-width="3" fill="none"/></svg></li>
      <li>Holstentor <svg class="tick" viewBox="0 0 16 13"><path d="M2 7 L6 11 L14 1" stroke="#0d3f73" stroke-width="3" fill="none"/></svg></li>
      <li>Heiligen Geist Hospital <svg class="tick" viewBox="0 0 16 13"><path d="M2 7 L6 11 L14 1" stroke="#0d3f73" stroke-width="3" fill="none"/></svg></li>
    </ul>
  </section>

  <section class="column column--bucht">
    <h2 class="column__title">Erlebins über<br>der <strong>Lübecker Bucht.</strong></h2>
    <p class="column__lead"><strong>Die Sightseeingtour über Lübeck, Ostsee und Umgebung.</strong> Ein Rundflug über die farbenfrohe Ferienregion rund um Lübeck ist genau das Richtige für alle, die das historische Lübeck und die moderne Küstengebiete bestaunen wollen.</p>
    <ul class="highlights">
      <li>Hansestadt Lübeck <svg class="tick" viewBox="0 0 16 13"><path d="M2 7 L6 11 L14 1" stroke="#0d3f73" stroke-width="3" fill="none"/></svg></li>
      <li>Travemünde <svg class="tick" viewBox="0 0 16 13"><path d="M2 7 L6 11 L14 1" stroke="#0d3f73" stroke-width="3" fill="none"/></svg></li>
      <li>Brodtener Steilküste <svg class="tick" viewBox="0 0 16 13"><path d="M2 7 L6 11 L14 1" stroke="#0d3f73" stroke-width="3" fill="none"/></svg></li>
      <li>Timmendorfer Strand <svg class="tick" viewBox="0 0 16 13"><path d="M2 7 L6 11 L14 1" stroke="#0d3f73" stroke-width="3" fill="none"/></svg></li>
      <li>Kiekpark Sierksdorf <svg class="tick" viewBox="0 0 16 13"><path d="M2 7 L6 11 L14 1" stroke="#0d3f73" stroke-width="3" fill="none"/></svg></li>
      <li>Yachthafen Neustadt i. H. <svg class="tick" viewBox="0 0 16 13"><path d="M2 7 L6 11 L14 1" stroke="#0d3f73" stroke-width="3" fill="none"/></svg></li>
    </ul>
  </section>

  <section class="column column--hamburg">
    <h2 class="column__title">Erlebins über <strong>Lübeck</strong><br>und <strong>Hamburg.</strong></h2>
    <p class="column__lead"><strong>Sie möchten einen einzigartigen Flug zwischen Tradition und Moderne erleben?</strong> Steigen Sie ein und überfliegen Sie ab Lübeck die Hanse- und Metropolstadt Hamburg an der Elbe. Ein faszinierender Flug mit allen Highlights.</p>
    <ul class="highlights">
      <li>Stadtinsel Lübeck <svg class="tick" viewBox="0 0 16 13"><path d="M2 7 L6 11 L14 1" stroke="#0d3f73" stroke-width="3" fill="none"/></svg></li>
      <li>St.Pauli <svg class="tick" viewBox="0 0 16 13"><path d="M2 7 L6 11 L14 1" stroke="#0d3f73" stroke-width="3" fill="none"/></svg></li>
      <li>Hamburger Hafen <svg class="tick" viewBox="0 0 16 13"><path d="M2 7 L6 11 L14 1" stroke="#0d3f73" stroke-width="3" fill="none"/></svg></li>
      <li>Altona Fischmarkt <svg class="tick" viewBox="0 0 16 13"><path d="M2 7 L6 11 L14 1" stroke="#0d3f73" stroke-width="3" fill="none"/></svg></li>
      <li>Jungfernstieg/Alster <svg class="tick" viewBox="0 0 16 13"><path d="M2 7 L6 11 L14 1" stroke="#0d3f73" stroke-width="3" fill="none"/></svg></li>
      <li>Flughaf. Hamburg/Aerovanta-Werk Finkenwerder <svg class="tick" viewBox="0 0 16 13"><path d="M2 7 L6 11 L14 1" stroke="#0d3f73" stroke-width="3" fill="none"/></svg></li>
    </ul>
  </section>

  <div class="photo photo--wing" role="img" aria-label="Blick aus dem Flugzeug über die Tragfläche auf Küste und Ostsee"></div>

  <div class="badge badge--30"><span class="badge__label">Dauer:</span><span class="badge__time">30 Min.</span><span class="badge__pax">Max.<br>3 Pers.</span></div>
  <div class="badge badge--45"><span class="badge__label">Dauer:</span><span class="badge__time">45 Min.</span><span class="badge__pax">Max.<br>3 Pers.</span></div>
  <div class="badge badge--60"><span class="badge__label">Dauer:</span><span class="badge__time">60 Min.</span><span class="badge__pax">Max.<br>3 Pers.</span></div>
</div>
</body>
</html>
```